Business Cards for a law firm

Business cards for our law firm. Use our silhoette logo and OAK HARBOR - check our website (www.oakharbor-legal.com)

Contact Information for Business Card

our silhouette logo, OAK HARBOR, 800-555-0147, Dorian Kestrup, dorian@oakharbor-legal.com

Requirements
Must have
• our silhouette logo, OAK HARBOR, 800-555-0147, Dorian Kestrup, dorian@oakharbor-legal.com

```html
<!DOCTYPE html>
<html lang="en">
<head>
<meta charset="utf-8">
<title>Oak Harbor – Business Card</title>
<link href="https://fonts.googleapis.com/css2?family=Cinzel:wght@500;600&family=Arimo:wght@400&display=swap" rel="stylesheet">
<style>
  :root {
    --backdrop: #3d3d3d;
    --paper: #ffffff;
    --navy: #1b3168;
    --navy-ink: #1d2f6b;
    --rule: #9aa0a8;
    --contact-ink: #4a4a4a;
    --logo-ink: #ffffff;
  }
  * { margin: 0; padding: 0; box-sizing: border-box; }
  html, body {
    width: 1200px;
    height: 803px;
    overflow: hidden;
    background: var(--backdrop);
  }
  .sheet {
    position: relative;
    width: 1200px;
    height: 803px;
    display: flex;
    align-items: center;
    justify-content: center;
    gap: 60px;
  }
  .card {
    width: 490px;
    height: 280px;
    border-radius: 18px;
    position: relative;
    box-shadow: 0 14px 30px rgba(0,0,0,0.35);
  }
  .card--front {
    background: var(--paper);
    display: flex;
    align-items: center;
    justify-content: center;
    gap: 18px;
  }
  .holder-name {
    font-family: "Cinzel", serif;
    font-weight: 600;
    font-size: 21px;
    letter-spacing: 1px;
    color: var(--navy-ink);
    white-space: nowrap;
  }
  .divider {
    width: 1px;
    height: 46px;
    background: var(--rule);
  }
  .contact-list {
    list-style: none;
    font-family: "Arimo", sans-serif;
    font-size: 12.5px;
    color: var(--contact-ink);
    line-height: 17px;
  }
  .contact-list li {
    display: flex;
    align-items: center;
    gap: 6px;
  }
  .contact-icon {
    width: 10px;
    height: 10px;
    flex: none;
  }
  .card--back {
    background: var(--navy);
    display: flex;
    align-items: center;
    justify-content: center;
    gap: 16px;
  }
  .logo-square {
    width: 22px;
    height: 22px;
    background: var(--logo-ink);
  }
  .firm-name {
    font-family: "Cinzel", serif;
    font-weight: 500;
    font-size: 34px;
    letter-spacing: 4px;
    color: var(--logo-ink);
    white-space: nowrap;
  }
</style>
</head>
<body>
<main class="sheet">
  <section class="card card--front" aria-label="Business card front">
    <p class="holder-name">Dorian Kestrup</p>
    <span class="divider"></span>
    <ul class="contact-list">
      <li>
        <svg class="contact-icon" viewBox="0 0 10 10" aria-hidden="true"><path d="M2 0.5 L3.6 2.6 L2.6 3.6 Q3.6 5.8 6.2 7.2 L7.2 6.2 L9.5 7.8 L8.3 9.5 Q3.5 9 0.5 2.2 Z" fill="var(--navy-ink)"/></svg>
        800-555-0147
      </li>
      <li>
        <svg class="contact-icon" viewBox="0 0 10 10" aria-hidden="true"><rect x="0.5" y="2" width="9" height="6.5" fill="var(--navy-ink)"/><path d="M0.8 2.3 L5 5.6 L9.2 2.3" stroke="#fff" stroke-width="0.9" fill="none"/></svg>
        dorian@oakharbor-legal.com
      </li>
      <li>
        <svg class="contact-icon" viewBox="0 0 10 10" aria-hidden="true"><circle cx="5" cy="5" r="4.5" fill="var(--navy-ink)"/><path d="M0.5 5 H9.5 M5 0.5 Q2.5 5 5 9.5 M5 0.5 Q7.5 5 5 9.5" stroke="#fff" stroke-width="0.6" fill="none"/></svg>
        www.oakharbor-legal.com
      </li>
    </ul>
  </section>

  <section class="card card--back" aria-label="Business card back">
    <span class="logo-square" aria-hidden="true"></span>
    <p class="firm-name">OAK HARBOR</p>
  </section>
</main>
</body>
</html>
```